Business Card for Quillmark Ledger - A cannabis publication for executives.

I'd like some business cards for Quillmark Ledger. The logo is done (great job!) and I need a card design I will use with PRINTLY. I made it a short project to allow time for printing before an event. These will be standard sized cards (final artwork size 3.66" x 2.16" at 300dpi) with a final card size of 3.5" x 2.0". (See PRINTLY.com if you need more info.) I might try rounded corners but am not sure yet. I think the design will work okay with rounded.

Quillmark Ledger will be a bi-weekly publication for the cannabis industry. It is targeted to investors and industry executives, not consumers or pot smokers. So our market is more B2B. However I am open to creativity and making the card something people remark on.

My contact for card:

Dana Merrow
Founder/CEO
dana@quillmarkledger.example

2740 Harlow Avenue
Boston MA 02135
(617)555-0194

Target Market(s)

Executives, Industry people and investors in the Cannabis sector.

Contact Information for Business Card

PRINTLY does do double sided and the second side can be the same or different images. Only one side is required but use of the second side would be a bonus.

Font styles to use
Serif
Sans Serif
Decorative

Colors

Designer to choose colors to be used in the design.

Requirements
Must have
• Logo, contact info
Nice to have
• Style and design to make the card stand out in a crowd.

```html
<!DOCTYPE html>
<html lang="en">
<head>
<meta charset="utf-8">
<title>Quillmark Ledger — Business Card</title>
<link href="https://fonts.googleapis.com/css2?family=Open+Sans:wght@400;600;700&display=swap" rel="stylesheet">
<style>
  :root {
    --page-bg: #e9e7e3;
    --card-white: #ffffff;
    --brand-blue: #0a74bb;
    --brand-green: #82b242;
    --text-white: #ffffff;
    --card-shadow: 0 10px 24px rgba(0,0,0,0.22);
  }
  * { box-sizing: border-box; margin: 0; padding: 0; }
  html, body { width: 1200px; height: 1000px; overflow: hidden; }
  body {
    background: var(--page-bg);
    font-family: "Open Sans", Arial, sans-serif;
    position: relative;
  }
  .card {
    position: absolute;
    width: 540px;
    height: 310px;
    border-radius: 22px;
    overflow: hidden;
    box-shadow: var(--card-shadow);
  }
  .card-front { left: 130px; top: 150px; background: var(--card-white); }
  .card-back { left: 530px; top: 530px; background: var(--brand-green); }
  .card-art { position: absolute; inset: 0; width: 100%; height: 100%; }

  .wordmark {
    position: absolute;
    display: flex;
    align-items: center;
    gap: 10px;
    font-weight: 700;
    white-space: nowrap;
  }
  .front-wordmark { right: 26px; top: 40px; color: var(--brand-blue); font-size: 30px; }
  .front-wordmark .mark-square { width: 22px; height: 22px; background: var(--brand-green); }

  .holder { position: absolute; left: 34px; top: 196px; color: var(--text-white); }
  .holder-name { font-weight: 700; font-size: 22px; letter-spacing: 0.3px; text-transform: uppercase; }
  .holder-title { font-size: 17px; margin-top: 0; }

  .contact-list {
    position: absolute; left: 292px; top: 156px;
    list-style: none; color: var(--text-white); font-size: 14.5px; line-height: 21px;
  }
  .contact-list li { display: flex; align-items: flex-start; gap: 8px; }
  .contact-list svg { width: 14px; height: 14px; margin-top: 4px; flex: none; fill: var(--text-white); }
  .contact-list .indent { padding-left: 22px; }

  .back-wordmark {
    left: 0; right: 0; top: 112px; justify-content: center;
    color: var(--text-white); font-size: 34px;
  }
  .back-wordmark .mark-circle { width: 26px; height: 26px; border-radius: 50%; background: var(--brand-blue); }
  .web-address {
    position: absolute; left: 0; right: 0; bottom: 22px;
    text-align: center; color: var(--text-white); font-size: 14px;
  }
</style>
</head>
<body>

  <section class="card card-front" aria-label="Business card front">
    <svg class="card-art" viewBox="0 0 540 310" aria-hidden="true">
      <rect class="blue-band" x="0" y="134" width="540" height="138" fill="var(--brand-blue)"/>
      <rect class="green-rule" x="0" y="127" width="540" height="8" fill="var(--brand-green)"/>
      <polygon class="notch-tab" points="76,129 136,129 136,158 122,172 90,172 76,158"
               fill="var(--card-white)" stroke="var(--brand-green)" stroke-width="6" stroke-linejoin="round"/>
      <g class="bubble-dots">
        <circle cx="100" cy="36" r="5" fill="var(--brand-blue)"/>
        <circle cx="98" cy="60" r="5.5" fill="var(--brand-green)"/>
        <circle cx="114" cy="70" r="5.5" fill="var(--brand-green)"/>
        <circle cx="106" cy="94" r="5" fill="var(--brand-blue)"/>
      </g>
    </svg>

    <div class="wordmark front-wordmark"><span class="mark-square"></span>Quillmark Ledger</div>

    <div class="holder">
      <p class="holder-name">Dana Merrow</p>
      <p class="holder-title">Founder/CEO</p>
    </div>

    <ul class="contact-list">
      <li>
        <svg viewBox="0 0 24 24"><path d="M6.6 10.8a15.1 15.1 0 0 0 6.6 6.6l2.2-2.2a1 1 0 0 1 1-.25 11.4 11.4 0 0 0 3.6.57 1 1 0 0 1 1 1V20a1 1 0 0 1-1 1A17 17 0 0 1 3 4a1 1 0 0 1 1-1h3.5a1 1 0 0 1 1 1c0 1.25.2 2.45.57 3.57a1 1 0 0 1-.25 1z"/></svg>
        (617) 555-0194
      </li>
      <li>
        <svg viewBox="0 0 24 24"><path d="M2 5h20v14H2z M2 5l10 8 10-8" fill="var(--text-white)"/><path d="M3 6l9 7 9-7" fill="none" stroke="var(--brand-blue)" stroke-width="2"/></svg>
        dana@quillmarkledger.example
      </li>
      <li>
        <svg viewBox="0 0 24 24"><path d="M12 2a7 7 0 0 0-7 7c0 5.2 7 13 7 13s7-7.8 7-13a7 7 0 0 0-7-7zm0 9.5A2.5 2.5 0 1 1 12 6.5a2.5 2.5 0 0 1 0 5z"/></svg>
        2740 Harlow Avenue
      </li>
      <li class="indent">Boston MA 02135</li>
    </ul>
  </section>

  <section class="card card-back" aria-label="Business card back">
    <svg class="card-art" viewBox="0 0 540 310" aria-hidden="true">
      <g class="bubble-dots-left">
        <circle cx="52" cy="112" r="6" fill="var(--brand-blue)"/>
        <circle cx="64" cy="138" r="6.5" fill="var(--card-white)"/>
        <circle cx="46" cy="154" r="6.5" fill="var(--card-white)"/>
        <circle cx="58" cy="180" r="6" fill="var(--brand-blue)"/>
      </g>
      <g class="bubble-dots-right">
        <circle cx="466" cy="112" r="6" fill="var(--brand-blue)"/>
        <circle cx="456" cy="138" r="6.5" fill="var(--card-white)"/>
        <circle cx="474" cy="154" r="6.5" fill="var(--card-white)"/>
        <circle cx="462" cy="180" r="6" fill="var(--brand-blue)"/>
      </g>
    </svg>

    <div class="wordmark back-wordmark"><span class="mark-circle"></span>Quillmark Ledger</div>

    <p class="web-address">www.quillmarkledger.example</p>
  </section>

</body>
</html>
```